Coralview Health Academy Open House

We need to create an advertisement for an upcoming open house that we are conducting. We can create a design in the dimensions of 10" (w) x 13.67" (h). Once that is approved, I will need the ad resized in the following dimensions:

8.5" (w) x 11" (h) - PDF
2400 pixels wide X 2400 pixels height - JPEG

Target Market(s)

Aspiring medical students

Industry/Entity Type

Medical

Requirements
Must have
• Logo
• Tag line: STUDY MEDICINE IN THE CARIBBEAN, BECOME A DOC IN THE US
• One of the attachments has a JPEG file with all the information to include in this new ad however the event location has changed to this:
• Sunday, April 22nd at 1pm at:
• Lantern Lodge Chicago Depot Square
• 718 N. Birch Court
• Chicago, IL 60654
• Event will be held on the 15th floor in The Penwick Room
• FREE parking. Refreshments will be served.
• Change email to admissions@chaheal.org
• Use a nice background and creative design. The details of the event need to be big and emphasize OPEN HOUSE.

```html
<!DOCTYPE html>
<html lang="en">
<head>
<meta charset="utf-8">
<title>Coralview Health Academy – Open House</title>
<link rel="stylesheet" href="https://fonts.googleapis.com/css2?family=PT+Sans:ital,wght@0,400;0,700;1,700&family=PT+Sans+Narrow:wght@700&family=Roboto+Condensed:wght@300;700&display=swap">
<style>
  :root {
    --navy: #0b2f63;
    --blue: #1455a8;
    --blue-bright: #1f6cc4;
    --red: #d61f36;
    --red-dark: #b3122a;
    --white: #ffffff;
    --ink: #1d2f5a;
  }
  * { margin: 0; padding: 0; box-sizing: border-box; }
  html, body { width: 1200px; height: 1195px; overflow: hidden; }
  body {
    position: relative;
    font-family: "PT Sans", sans-serif;
    background: linear-gradient(180deg, var(--blue) 0%, var(--navy) 100%);
    color: var(--white);
  }
  .band-top, .band-bottom {
    position: absolute; left: 0; width: 1200px;
    background: linear-gradient(90deg, var(--red-dark), var(--red), var(--red-dark));
  }
  .band-top { top: 0; height: 20px; }
  .band-bottom { top: 1176px; height: 19px; }

  .title-panel {
    position: absolute; left: 0; top: 20px; width: 436px; height: 262px;
    background: radial-gradient(circle at 75% 60%, var(--blue-bright) 0%, var(--blue) 35%, var(--navy) 100%);
  }
  .title-open, .title-houses {
    position: absolute; left: 42px;
    font-family: "Roboto Condensed", sans-serif; line-height: 1; letter-spacing: -1px;
  }
  .title-open { top: 42px; font-size: 86px; font-weight: 300; }
  .title-houses { top: 140px; font-size: 96px; font-weight: 700; }

  .events-panel {
    position: absolute; left: 436px; top: 20px; width: 764px; height: 262px;
    background: var(--white);
  }
  .event { position: absolute; left: 89px; top: 46px; color: var(--ink); }
  .event-date { color: var(--red); font-weight: 700; font-size: 38px; line-height: 46px; margin-bottom: 6px; }
  .event-place { font-size: 24px; line-height: 31px; }
  .event-room { font-size: 24px; line-height: 31px; font-weight: 700; }

  .perk-seal { position: absolute; left: 973px; top: 50px; width: 216px; height: 216px; }
  .perk-text {
    position: absolute; left: 973px; top: 118px; width: 216px;
    text-align: center; font-size: 19px; line-height: 30px; color: var(--white);
  }

  .hero-photo {
    position: absolute; left: 0; top: 282px; width: 1200px; height: 495px;
    border-bottom-right-radius: 80px;
    background:
      radial-gradient(ellipse 22% 42% at 66% 55%, #2d7cc9 0%, rgba(45,124,201,0) 100%),
      radial-gradient(ellipse 12% 18% at 66% 28%, #8a5a3c 0%, rgba(138,90,60,0) 100%),
      linear-gradient(90deg, #2a4d86 0%, #6d7ea0 28%, #b79a72 50%, #a98560 70%, #4f7cb8 100%);
  }
  .tagline {
    position: absolute; left: 38px; top: 310px;
    font-family: "PT Sans Narrow", sans-serif; font-weight: 700;
    font-size: 68px; line-height: 73px; text-transform: uppercase;
    text-shadow: 0 2px 6px rgba(0,0,0,.45);
  }

  .brand-mark {
    position: absolute; left: 93px; top: 623px; width: 224px; height: 224px;
    border-radius: 50%; background: var(--white);
    display: flex; align-items: center; justify-content: center;
    box-shadow: 0 3px 10px rgba(0,0,0,.35);
  }
  .brand-name {
    width: 150px; text-align: center; color: var(--navy);
    font-weight: 700; font-size: 24px; line-height: 28px;
  }

  .fee-offer {
    position: absolute; left: 0; top: 862px; width: 410px;
    text-align: center; font-weight: 700; font-size: 20px; line-height: 38px;
  }
  .coupon-code {
    position: absolute; left: 117px; top: 981px; width: 175px; height: 35px;
    border-radius: 18px; background: var(--red);
    display: flex; align-items: center; justify-content: center;
    font-weight: 700; font-size: 22px; letter-spacing: 3px;
    box-shadow: 0 2px 4px rgba(0,0,0,.3);
  }

  .features-card {
    position: absolute; left: 470px; top: 777px; width: 730px; height: 307px;
    background: var(--white); border-bottom-left-radius: 80px;
  }
  .feature-list { position: absolute; left: 64px; top: 11px; list-style: none; color: var(--ink); }
  .feature-list li {
    display: flex; align-items: center; height: 35px; font-size: 26px;
  }
  .feature-list svg { width: 22px; height: 22px; margin-right: 24px; flex: none; }
  .feature-list small { font-size: 19px; margin-left: 6px; }

  .rsvp {
    position: absolute; left: 28px; top: 1066px;
    color: var(--red); font-style: italic; font-weight: 700; font-size: 32px;
  }
  .contact {
    position: absolute; top: 1120px; display: flex; align-items: center;
    font-size: 30px; font-weight: 700;
  }
  .contact svg { width: 28px; height: 28px; margin-right: 12px; }
  .contact-email { left: 22px; }
  .contact-phone { left: 523px; }
  .contact-web { left: 850px; }
</style>
</head>
<body>
  <div class="band-top"></div>

  <section class="title-panel">
    <div class="title-open">OPEN</div>
    <div class="title-houses">HOUSES</div>
  </section>

  <section class="events-panel">
    <div class="event">
      <div class="event-date">Sunday, April 22nd at 1pm</div>
      <div class="event-place">Lantern Lodge Chicago Depot Square</div>
      <div class="event-place">718 N. Birch Court, Chicago, IL 60654</div>
      <div class="event-room">15th floor, The Penwick Room</div>
    </div>
  </section>

  <svg class="perk-seal" viewBox="-110 -110 220 220" aria-hidden="true">
    <defs>
      <radialGradient id="sealFill" cx="50%" cy="45%" r="60%">
        <stop offset="0" stop-color="#1d5fb0"/>
        <stop offset="1" stop-color="#0a2a5a"/>
      </radialGradient>
    </defs>
    <polygon fill="url(#sealFill)" points="0,-108 12,-97 28,-104 36,-91 53,-94 57,-79 74,-78 74,-62 89,-57 85,-42 98,-33 90,-19 99,-5 88,6 94,21 81,29 83,45 68,50 66,66 50,67 44,83 29,80 19,93 6,86 -6,99 -17,88 -31,96 -38,82 -54,84 -57,69 -73,67 -73,51 -88,45 -83,31 -96,21 -88,8 -98,-5 -88,-16 -93,-31 -80,-38 -81,-54 -65,-58 -63,-74 -47,-75 -40,-90 -25,-86 -14,-99"/>
  </svg>
  <div class="perk-text">FREE parking.<br>Refreshments will<br>be served.</div>

  <div class="hero-photo" role="img" aria-label="Photo of a smiling medical student in blue scrubs with a stethoscope and clipboard, classmates in scrubs talking in a hallway behind her"></div>

  <h1 class="tagline">Study medicine<br>in the Caribbean,<br>become a doc<br>in the US</h1>

  <div class="brand-mark">
    <span class="brand-name">Coralview Health Academy</span>
  </div>

  <p class="fee-offer">HAVE YOUR ENTIRE<br>APPLICATION FEE WAIVED!<br>ENTER COUPON CODE:</p>
  <div class="coupon-code">OPHUS</div>

  <section class="features-card">
    <ul class="feature-list">
      <li><svg viewBox="0 0 22 22"><circle cx="11" cy="11" r="9" fill="none" stroke="#d61f36" stroke-width="2"/><path d="M6.5 10.5l3.5 3.5 7-8" fill="none" stroke="#d61f36" stroke-width="2.2"/></svg>4 Years MD Program</li>
      <li><svg viewBox="0 0 22 22"><circle cx="11" cy="11" r="9" fill="none" stroke="#d61f36" stroke-width="2"/><path d="M6.5 10.5l3.5 3.5 7-8" fill="none" stroke="#d61f36" stroke-width="2.2"/></svg>Financial Aid</li>
      <li><svg viewBox="0 0 22 22"><circle cx="11" cy="11" r="9" fill="none" stroke="#d61f36" stroke-width="2"/><path d="M6.5 10.5l3.5 3.5 7-8" fill="none" stroke="#d61f36" stroke-width="2.2"/></svg>Student Dorms</li>
      <li><svg viewBox="0 0 22 22"><circle cx="11" cy="11" r="9" fill="none" stroke="#d61f36" stroke-width="2"/><path d="M6.5 10.5l3.5 3.5 7-8" fill="none" stroke="#d61f36" stroke-width="2.2"/></svg>Modern Campus</li>
      <li><svg viewBox="0 0 22 22"><circle cx="11" cy="11" r="9" fill="none" stroke="#d61f36" stroke-width="2"/><path d="M6.5 10.5l3.5 3.5 7-8" fill="none" stroke="#d61f36" stroke-width="2.2"/></svg>Friendly Tution <small>($5,900/semester)</small></li>
      <li><svg viewBox="0 0 22 22"><circle cx="11" cy="11" r="9" fill="none" stroke="#d61f36" stroke-width="2"/><path d="M6.5 10.5l3.5 3.5 7-8" fill="none" stroke="#d61f36" stroke-width="2.2"/></svg>U.S Clinical Rotations</li>
      <li><svg viewBox="0 0 22 22"><circle cx="11" cy="11" r="9" fill="none" stroke="#d61f36" stroke-width="2"/><path d="M6.5 10.5l3.5 3.5 7-8" fill="none" stroke="#d61f36" stroke-width="2.2"/></svg>88.9% USMLE Passing Rate</li>
      <li><svg viewBox="0 0 22 22"><circle cx="11" cy="11" r="9" fill="none" stroke="#d61f36" stroke-width="2"/><path d="M6.5 10.5l3.5 3.5 7-8" fill="none" stroke="#d61f36" stroke-width="2.2"/></svg>Canadian Loans Available</li>
    </ul>
  </section>

  <div class="rsvp">Please RSVP by email</div>

  <div class="contact contact-email">
    <svg viewBox="0 0 28 28"><circle cx="14" cy="14" r="12.5" fill="none" stroke="#d61f36" stroke-width="2.5"/><rect x="7.5" y="9.5" width="13" height="9" fill="#d61f36"/><path d="M7.5 9.5l6.5 5 6.5-5" fill="none" stroke="#0b2f63" stroke-width="1.5"/></svg>
    admissions@chaheal.org
  </div>
  <div class="contact contact-phone">
    <svg viewBox="0 0 28 28"><circle cx="14" cy="14" r="12.5" fill="none" stroke="#d61f36" stroke-width="2.5"/><path d="M9.5 7.5l3 3-1.8 2.2c1 2 2.6 3.6 4.6 4.6l2.2-1.8 3 3-2 2.2c-5.5-.6-10.6-5.7-11.2-11.2z" fill="#d61f36"/></svg>
    888-555-0142
  </div>
  <div class="contact contact-web">
    <svg viewBox="0 0 28 28"><circle cx="14" cy="14" r="12.5" fill="none" stroke="#d61f36" stroke-width="2.5"/><circle cx="14" cy="14" r="7.5" fill="none" stroke="#d61f36" stroke-width="1.5"/><ellipse cx="14" cy="14" rx="3.2" ry="7.5" fill="none" stroke="#d61f36" stroke-width="1.5"/><path d="M6.5 14h15M8 10h12M8 18h12" stroke="#d61f36" stroke-width="1.3"/></svg>
    www.chaheal.org
  </div>

  <div class="band-bottom"></div>
</body>
</html>
```